I need a business Card Design for my practice , i am clinical herbalist. I am a herbalist specializing in Lyme disease, autism, autoimmune diseases, difficult to cure diseasesDifficult to cure diseases. In my innovative practice i link traditional medicine, herbs with science, immunologu ,pharmacology.

Industry/Entity Type

Business

Contact Information for Business Card

My company name : OSRODEK ZIELNIKA
My name : Piotr Weltak
Name of my profession : Fitoterapeuta
In Polish language Fitoterapeuta is Herbalist .

e-mail: piotrweltak@osrodekzielnika.com
www.osrodek-zielnika.pl
phone : 574 806 215
My company adress : Dąbrowa Sękowska 14 , 38-415 Mielnik
I dont have logo .

Requirements
Nice to have
• My company

```html
<!DOCTYPE html>
<html lang="pl">
<head>
<meta charset="utf-8">
<title>Osrodek Zielnika – wizytówka</title>
<link rel="stylesheet" href="https://fonts.googleapis.com/css2?family=Cinzel:wght@500;600&family=Montserrat:wght@400;500;600&display=swap">
<style>
  :root {
    --page-bg: #2b2c2d;
    --leaf-green: #55823a;
    --deep-green: #4b7a2f;
    --fresh-green: #7fb83a;
    --paper: #ffffff;
    --ink-grey: #7a7a7a;
    --ink-dark: #6a6a6a;
  }
  * { box-sizing: border-box; margin: 0; padding: 0; }
  html, body {
    width: 1200px; height: 864px; overflow: hidden;
    background: var(--page-bg);
  }
  .sheet {
    width: 1200px; height: 864px;
    display: flex; flex-direction: column;
    align-items: center; justify-content: center; gap: 36px;
  }
  .card {
    position: relative;
    width: 700px; height: 400px;
    border-radius: 22px;
    box-shadow: 0 10px 28px rgba(0,0,0,.45);
  }
  .card--front { background: var(--leaf-green); color: var(--paper); }
  .card--back { background: var(--paper); }

  .brand-name {
    font-family: "Cinzel", serif;
    font-weight: 500;
    letter-spacing: 1px;
    white-space: nowrap;
  }
  .card--front .brand-name {
    position: absolute; left: 0; right: 0; top: 148px;
    text-align: center; font-size: 50px; color: var(--paper);
  }
  .front-web {
    position: absolute; left: 0; right: 0; bottom: 52px;
    text-align: center;
    font-family: "Montserrat", sans-serif; font-size: 15px;
    color: var(--paper);
  }

  .card--back .brand-name {
    position: absolute; right: 44px; top: 40px;
    font-size: 46px; color: var(--deep-green);
  }
  .contact {
    position: absolute; left: 56px; bottom: 40px;
    font-family: "Montserrat", sans-serif; color: var(--ink-grey);
  }
  .person-name { font-size: 28px; font-weight: 600; color: var(--deep-green); line-height: 1.05; }
  .person-role { font-size: 17px; margin-bottom: 14px; }
  .company { font-size: 17px; font-weight: 600; color: var(--ink-dark); text-transform: uppercase; }
  .address { font-size: 17px; margin-bottom: 12px; }
  .contact-list { list-style: none; font-size: 17px; }
  .contact-list li { display: flex; align-items: center; gap: 10px; line-height: 1.45; }
  .contact-list svg { width: 18px; height: 18px; fill: var(--fresh-green); flex: none; }
</style>
</head>
<body>
<main class="sheet">
  <section class="card card--front" aria-label="Przód wizytówki">
    <h1 class="brand-name">Osrodek Zielnika</h1>
    <p class="front-web">www.osrodek-zielnika.pl</p>
  </section>

  <section class="card card--back" aria-label="Tył wizytówki">
    <h2 class="brand-name">Osrodek Zielnika</h2>
    <div class="contact">
      <p class="person-name">Piotr Weltak</p>
      <p class="person-role">Fitoterapeuta</p>
      <p class="company">Osrodek Zielnika</p>
      <p class="address">Dąbrowa Sękowska 14 , 38-415 Mielnik</p>
      <ul class="contact-list">
        <li>
          <svg viewBox="0 0 24 24" aria-hidden="true"><path d="M6.6 10.8a15.1 15.1 0 0 0 6.6 6.6l2.2-2.2c.3-.3.7-.4 1-.2 1.1.4 2.3.6 3.6.6.6 0 1 .4 1 1V20c0 .6-.4 1-1 1A17 17 0 0 1 3 4c0-.6.4-1 1-1h3.5c.6 0 1 .4 1 1 0 1.3.2 2.5.6 3.6.1.3 0 .7-.2 1z"/></svg>
          574 806 215
        </li>
        <li>
          <svg viewBox="0 0 24 24" aria-hidden="true"><path d="M2 5h20v14H2z M2 5l10 8 10-8" /><path d="M3 6.2v11.8h18V6.2l-9 7.2z" fill="#fff" opacity="0"/></svg>
          piotrweltak@osrodekzielnika.com
        </li>
        <li>
          <svg viewBox="0 0 24 24" aria-hidden="true"><path d="M12 2a10 10 0 1 0 0 20 10 10 0 0 0 0-20zm6.9 6h-3a15.6 15.6 0 0 0-1.3-3.6A8 8 0 0 1 18.9 8zM12 4c.8 1.2 1.5 2.5 1.9 4h-3.8c.4-1.5 1.1-2.8 1.9-4zM4.3 14a8 8 0 0 1 0-4h3.4a16 16 0 0 0 0 4zm.8 2h3a15.6 15.6 0 0 0 1.3 3.6A8 8 0 0 1 5.1 16zm3-8h-3a8 8 0 0 1 4.3-3.6C8.8 5.6 8.4 6.8 8.1 8zM12 20c-.8-1.2-1.5-2.5-1.9-4h3.8c-.4 1.5-1.1 2.8-1.9 4zm2.3-6H9.7a14.7 14.7 0 0 1 0-4h4.6a14.7 14.7 0 0 1 0 4zm.3 5.6c.6-1.1 1-2.3 1.3-3.6h3a8 8 0 0 1-4.3 3.6zm1.7-5.6a16 16 0 0 0 0-4h3.4a8 8 0 0 1 0 4z"/></svg>
          www.osrodek-zielnika.pl
        </li>
      </ul>
    </div>
  </section>
</main>
</body>
</html>
```